The Plasterline & Soundcraft Partners Inc (PSPI)

Create a LOGO and Business Card design.

Colors: Black, Bright Yellow & Red

Description of company: commercial carpentry, metal framing, drywall, taping/spackling, demolition, rough/finish carpentry.

Target Market(s)

developers, architects, general contractors, construction managers

Industry/Entity Type

Business

```html
<!DOCTYPE html>
<html lang="en">
<head>
<meta charset="utf-8">
<title>PSPI Business Card</title>
<link rel="stylesheet" href="https://fonts.googleapis.com/css2?family=Open+Sans:wght@400;600&display=swap">
<style>
  :root {
    --ink: #000000;
    --paper: #ffffff;
    --accent-red: #ff0000;
    --accent-yellow: #ffff00;
  }
  * { margin: 0; padding: 0; box-sizing: border-box; }
  html, body {
    width: 1200px;
    height: 900px;
    overflow: hidden;
    background: var(--paper);
    font-family: "Open Sans", Arial, sans-serif;
  }
  .card {
    position: absolute;
    left: 110px;
    top: 128px;
    width: 1000px;
    height: 647px;
    border: 1px solid var(--ink);
    background: var(--paper);
  }
  .brand {
    position: absolute;
    left: 0;
    top: 0;
    width: 100%;
    height: 390px;
  }
  .brand-lockup {
    position: absolute;
    left: 0;
    right: 0;
    top: 168px;
    display: flex;
    justify-content: center;
    align-items: center;
    gap: 22px;
  }
  .brand-square {
    width: 40px;
    height: 40px;
    background: var(--accent-red);
  }
  .brand-name {
    font-size: 126px;
    font-weight: 400;
    line-height: 1;
    letter-spacing: 8px;
    color: var(--ink);
  }
  .brand-tagline {
    position: absolute;
    left: 0;
    right: 0;
    top: 307px;
    text-align: center;
    font-size: 17.5px;
    font-weight: 600;
    color: var(--ink);
  }
  .services {
    position: absolute;
    left: 0;
    top: 390px;
    width: 100%;
    height: 256px;
    background: var(--ink);
  }
  .service-list {
    position: absolute;
    top: 36px;
    list-style: none;
  }
  .service-list--left { left: 82px; }
  .service-list--right { left: 586px; }
  .service-item {
    display: flex;
    align-items: center;
    height: 60px;
    font-size: 28px;
    color: var(--paper);
  }
  .service-bullet {
    width: 22px;
    height: 22px;
    margin-right: 15px;
    flex: none;
  }
</style>
</head>
<body>
  <div class="card">
    <header class="brand">
      <div class="brand-lockup">
        <span class="brand-square" aria-hidden="true"></span>
        <span class="brand-name">PSPI</span>
      </div>
      <p class="brand-tagline">PLASTERLINE &amp; SOUNDCRAFT PARTNERS Inc</p>
    </header>
    <section class="services">
      <ul class="service-list service-list--left">
        <li class="service-item"><svg class="service-bullet" viewBox="0 0 22 22" aria-hidden="true"><polygon points="11,0 22,11 11,22 0,11" fill="var(--accent-yellow)"/></svg>commercial carpentry</li>
        <li class="service-item"><svg class="service-bullet" viewBox="0 0 22 22" aria-hidden="true"><polygon points="11,0 22,11 11,22 0,11" fill="var(--accent-yellow)"/></svg>metal framing</li>
        <li class="service-item"><svg class="service-bullet" viewBox="0 0 22 22" aria-hidden="true"><polygon points="11,0 22,11 11,22 0,11" fill="var(--accent-yellow)"/></svg>drywall</li>
      </ul>
      <ul class="service-list service-list--right">
        <li class="service-item"><svg class="service-bullet" viewBox="0 0 22 22" aria-hidden="true"><polygon points="11,0 22,11 11,22 0,11" fill="var(--accent-yellow)"/></svg>taping / spackling</li>
        <li class="service-item"><svg class="service-bullet" viewBox="0 0 22 22" aria-hidden="true"><polygon points="11,0 22,11 11,22 0,11" fill="var(--accent-yellow)"/></svg>demolition</li>
        <li class="service-item"><svg class="service-bullet" viewBox="0 0 22 22" aria-hidden="true"><polygon points="11,0 22,11 11,22 0,11" fill="var(--accent-yellow)"/></svg>rough / finish carpentry</li>
      </ul>
    </section>
  </div>
</body>
</html>
```